Private label Bottled water label design

We are launching private label water bottle case packs with our brand “brightway”
Need bottle labels design as well as case pack design artwork. Bottle is 16.9oz similar to pet calvora feltmoor bottles.
It will be spring water.
Case pack will be of 24 bottles
Brightway is a chain of convenience stores in Texas
www.brightwaymarkets.example
I have attached pictures of calvora water. It would be similar packaging for single and case pack.

Target Market(s)

Male female shoppers middle aged. Take home package or single serve in cold vault

Industry/Entity Type

Water bottle retail

Colors
0054AA
0677BA
7BADD7
CADEEF
E8F1F8
59FF00
82FF00
B8FF75
E3FFCB
F4FFEA

Requirements
Must have
• Very premium look. Use the logo of brightway
Nice to have
• Elegant premium water look
Should not have
• I am open to all

```html
<!DOCTYPE html>
<html lang="en">
<head>
<meta charset="utf-8">
<title>Brightway Spring Water – Bottle Label</title>
<link rel="stylesheet" href="https://fonts.googleapis.com/css2?family=Nunito:wght@900&family=Big+Shoulders+Display:wght@800&family=Oswald:wght@300&display=swap">
<style>
  :root {
    --label-blue: #05A4E4;
    --sky-light: #CFE9F4;
    --sky-blue: #7FC3E2;
    --canopy-dark: #1F5A4C;
    --canopy-mid: #2E7A62;
    --moss: #4E9A5E;
    --stream-teal: #2C8FA6;
    --stream-deep: #1B5F73;
    --splash-white: rgba(235, 246, 252, 0.9);
    --brand-white: #FFFFFF;
    --title-blue: #1548A2;
    --badge-line: rgba(255, 255, 255, 0.9);
    --badge-fill: rgba(255, 255, 255, 0.12);
  }
  html, body {
    margin: 0;
    padding: 0;
    width: 1200px;
    height: 190px;
    overflow: hidden;
    background: var(--label-blue);
  }
  .label {
    position: relative;
    width: 1200px;
    height: 190px;
    background: var(--label-blue);
    overflow: hidden;
  }
  .spring-scene {
    position: absolute;
    left: 336px;
    top: 0;
    width: 492px;
    height: 190px;
    background:
      radial-gradient(ellipse 22% 40% at 8% 55%, var(--splash-white) 0%, transparent 75%),
      radial-gradient(ellipse 7% 70% at 77% 30%, rgba(230, 245, 252, 0.75) 0%, transparent 80%),
      radial-gradient(ellipse 22% 22% at 52% 20%, var(--sky-light) 0%, transparent 80%),
      radial-gradient(ellipse 30% 35% at 30% 35%, var(--canopy-dark) 0%, transparent 75%),
      radial-gradient(ellipse 30% 35% at 75% 45%, var(--canopy-mid) 0%, transparent 75%),
      radial-gradient(ellipse 40% 25% at 50% 70%, var(--moss) 0%, transparent 80%),
      radial-gradient(ellipse 45% 25% at 55% 95%, var(--stream-teal) 0%, transparent 80%),
      linear-gradient(180deg, var(--sky-blue) 0%, var(--canopy-mid) 45%, var(--stream-deep) 100%);
    -webkit-mask-image: linear-gradient(90deg, transparent 0%, #000 10%, #000 88%, transparent 100%);
    mask-image: linear-gradient(90deg, transparent 0%, #000 10%, #000 88%, transparent 100%);
  }
  .brand-name {
    position: absolute;
    left: 0;
    width: 1200px;
    top: 44px;
    margin: 0;
    text-align: center;
    font-family: "Nunito", sans-serif;
    font-weight: 900;
    font-size: 44px;
    line-height: 48px;
    letter-spacing: -1.5px;
    color: var(--brand-white);
  }
  .product-title {
    position: absolute;
    left: 0;
    width: 1200px;
    top: 96px;
    margin: 0;
    text-align: center;
    font-family: "Big Shoulders Display", sans-serif;
    font-weight: 800;
    font-size: 62px;
    line-height: 58px;
    color: var(--title-blue);
    -webkit-text-stroke: 2px var(--brand-white);
    paint-order: stroke fill;
    filter: drop-shadow(1px 0 0 var(--title-blue)) drop-shadow(-1px 0 0 var(--title-blue)) drop-shadow(0 1px 0 var(--title-blue)) drop-shadow(0 -1px 0 var(--title-blue));
    white-space: nowrap;
  }
  .product-title span {
    display: inline-block;
    transform: scaleX(0.8);
  }
  .volume {
    position: absolute;
    left: 0;
    width: 1200px;
    top: 157px;
    margin: 0;
    text-align: center;
    font-family: "Oswald", sans-serif;
    font-weight: 300;
    font-size: 14px;
    line-height: 16px;
    color: var(--brand-white);
  }
  .quality-seal {
    position: absolute;
    left: 739px;
    top: 18px;
    width: 68px;
    height: 68px;
  }
</style>
</head>
<body>
  <main class="label">
    <div class="spring-scene" role="img" aria-label="Illustrated forest spring with a stream, tall trees, clouds and splashing water"></div>

    <div class="brand-name">brightway</div>

    <h1 class="product-title"><span>SPRING WATER</span></h1>

    <p class="volume">16oz/0.5L</p>

    <svg class="quality-seal" viewBox="0 0 68 68" aria-hidden="true">
      <circle cx="34" cy="34" r="32.5" fill="var(--badge-fill)" stroke="var(--badge-line)" stroke-width="1.6"/>
      <circle cx="34" cy="34" r="22" fill="none" stroke="var(--badge-line)" stroke-width="1.2"/>
      <circle cx="34" cy="34" r="16" fill="rgba(255,255,255,0.18)"/>
    </svg>
  </main>
</body>
</html>
```